Harold Brisk Mechanical business cards

We need business cards designed for "Harold Brisk Mechanical" "Mechanical & Electrical Contractors" "Specializing in Service & Installation"
"Cooling, Heating, Service, Installations, Residential, Commercial"

```html
<!DOCTYPE html>
<html lang="en">
<head>
<meta charset="utf-8">
<title>Harold Brisk Mechanical – Business Cards</title>
<link rel="stylesheet" href="https://fonts.googleapis.com/css2?family=Ubuntu:wght@400;500;700&family=Roboto:wght@400;500;700&display=swap">
<style>
  :root {
    --backdrop: #5b5b5b;
    --brand-red: #e8202a;
    --ink: #111111;
    --text-grey: #4a4a4a;
    --rule-grey: #d6d6d6;
    --paper: #ffffff;
  }
  * { margin: 0; padding: 0; box-sizing: border-box; }
  html, body { width: 1200px; height: 802px; overflow: hidden; }
  body { background: var(--backdrop); position: relative; font-family: "Roboto", Arial, sans-serif; }

  .card {
    position: absolute; top: 274px; width: 443px; height: 265px;
    box-shadow: 2px 3px 6px rgba(0,0,0,0.45);
  }
  .card-front { left: 136px; background: var(--paper); }
  .card-back { left: 624px; background: var(--brand-red); color: #fff; text-align: center; }

  /* front: brand block */
  .brand { position: absolute; left: 0; width: 224px; top: 80px; text-align: center; font-family: "Ubuntu", sans-serif; font-weight: 700; color: var(--ink); }
  .brand-mark { width: 62px; height: 50px; background: var(--brand-red); margin: 0 auto 12px; }
  .brand-name { font-size: 21px; letter-spacing: 0.5px; line-height: 1; }
  .brand-sub { font-size: 11px; letter-spacing: 4.2px; margin-top: 5px; line-height: 1; }

  .divider { position: absolute; left: 224px; top: 62px; width: 1px; height: 142px; background: var(--rule-grey); }

  .contact { position: absolute; left: 237px; top: 63px; color: var(--text-grey); }
  .person-name { font-family: "Ubuntu", sans-serif; font-weight: 500; font-size: 16px; color: var(--brand-red); line-height: 20px; }
  .person-role { font-size: 13px; line-height: 16px; margin-bottom: 5px; }
  .contact-list { list-style: none; font-size: 13px; line-height: 16px; }
  .contact-list li { display: flex; align-items: center; gap: 4px; }
  .contact-list svg { width: 10px; height: 10px; fill: var(--brand-red); flex: none; }
  .address { font-family: "Ubuntu", sans-serif; font-size: 13px; line-height: 16px; margin-top: 5px; }

  /* back */
  .back-pattern { position: absolute; inset: 0; background: linear-gradient(180deg, #ec2a33, #e61e28); }
  .back-content { position: relative; }
  .back-title { font-family: "Ubuntu", sans-serif; font-weight: 700; line-height: 1; }
  .back-title .line-1 { display: block; font-size: 35px; letter-spacing: 1.5px; padding-top: 60px; }
  .back-title .line-2 { display: block; font-size: 17px; letter-spacing: 7px; margin-top: 8px; padding-left: 7px; }
  .tagline { font-family: "Ubuntu", sans-serif; font-size: 13px; margin-top: 10px; letter-spacing: 0.2px; }
  .back-rule { width: 296px; height: 1px; background: rgba(255,255,255,0.45); margin: 8px auto 0; }
  .specialty { font-weight: 700; font-size: 13px; margin-top: 13px; line-height: 16px; }
  .services { font-size: 13px; line-height: 16px; }
</style>
</head>
<body>
  <section class="card card-front">
    <div class="brand">
      <div class="brand-mark"></div>
      <div class="brand-name">HAROLD BRISK</div>
      <div class="brand-sub">MECHANICAL</div>
    </div>
    <div class="divider"></div>
    <div class="contact">
      <div class="person-name">DORIAN PIKE</div>
      <div class="person-role">Managing Director</div>
      <ul class="contact-list">
        <li><svg viewBox="0 0 10 10"><path d="M1 3 Q5 0 9 3 L8 4.5 L6.5 3.6 L6.5 2.8 Q5 2.3 3.5 2.8 L3.5 3.6 L2 4.5Z M2.5 5 H7.5 L8.5 9 H1.5Z"/></svg>055-310 742 618</li>
        <li><svg viewBox="0 0 10 10"><path d="M2.5 0.5 H7.5 V9.5 H2.5Z M3.5 1.5 V7.5 H6.5 V1.5Z"/></svg>055-310 742 618</li>
        <li><svg viewBox="0 0 10 10"><path d="M0.5 2 H9.5 V8 H0.5Z" /><path d="M0.5 2 L5 5.5 L9.5 2" stroke="#fff" stroke-width="1" fill="none"/></svg>hello@haroldbrisk.com</li>
        <li><svg viewBox="0 0 10 10"><circle cx="5" cy="5" r="4.5"/><path d="M0.5 5 H9.5 M5 0.5 V9.5" stroke="#fff" stroke-width="0.8"/></svg>www.haroldbrisk.com</li>
      </ul>
      <div class="address">48 Foundry Lane, Unit 3<br>Westvale, 204871.</div>
    </div>
  </section>

  <section class="card card-back">
    <div class="back-pattern" role="img" aria-label="Repeating faint brand pattern in tones of red"></div>
    <div class="back-content">
      <h1 class="back-title"><span class="line-1">HAROLD BRISK</span><span class="line-2">MECHANICAL</span></h1>
      <p class="tagline">MECHANICAL &amp; ELECTRICAL CONTRACTORS</p>
      <div class="back-rule"></div>
      <p class="specialty">SPECIALIZING IN SERVICE &amp; INSTALLATION</p>
      <p class="services">Cooling | Heating | Service | Installations</p>
      <p class="services">Residential | Commercial</p>
    </div>
  </section>
</body>
</html>
```